The Harbourline Recruitment Company & Crestwork Staffing Office Warming

We are two recruitment firms located in the same offices (the Harbourline Recruitment Company & Crestwork Staffing) wanting to send out an e-vite like invitation design through outlook to our top clients for our office warming party/Christmas soiree December 6th.

We would like to see some orange and green (Harbourline Colours) and blue and green for Crestwork Staffing.

Logos to be included,
Date: Thursday December 6th from 4.30 - 7.30pm.
Address: 218 Kowhai Valley Road, Ellerslie

We will be forwarding this out in a mail message body to our clients in outlook. , We are two recruitment firms located in the same offices (the Harbourline Recruitment Company & Crestwork Staffing) wanting to send out an e-vite like invitation design through outlook to our top clients for our office warming party/Christmas soiree December 6th.

Logos to be included,

We will be forwarding this out in a mail message body to our clients in outlook.
Updates

Hi there

Please take note of the change in our deadline as we requrie designs asap.

Thanks again everyone!!  Look forward to reviewing.

Thanks

Penelope

Target Market(s)

Our top 100 clients

Industry/Entity Type

It Company

Requirements
Must have
• Logos
Date and Time
Address

```html
<!DOCTYPE html>
<html lang="en">
<head>
<meta charset="utf-8">
<title>Christmas Soiree Invitation – Crestwork Staffing &amp; The Harbourline Recruitment Company</title>
<link rel="stylesheet" href="https://fonts.googleapis.com/css2?family=Varela+Round&display=swap">
<style>
  :root {
    --night: #141414;
    --night-edge: #050505;
    --leaf-green: #8cc63f;
    --pale-green: #c9e7a0;
    --glow-blue: #2ea6e6;
    --ice-white: #f4f4f4;
    --gold: #c9a64a;
    --tree-green: #1f7a3a;
    --tree-blue: #1f8fc0;
    --card-white: #ffffff;
    --crestwork-blue: #1e88c8;
    --harbourline-orange: #f28c1e;
  }
  html, body {
    margin: 0;
    padding: 0;
    width: 1200px;
    height: 794px;
    overflow: hidden;
    background: var(--night-edge);
  }
  .invitation {
    position: relative;
    width: 1200px;
    height: 794px;
    overflow: hidden;
    background: radial-gradient(ellipse at 45% 45%, #262626 0%, var(--night) 55%, var(--night-edge) 100%);
    font-family: "Varela Round", "Arial Rounded MT Bold", sans-serif;
  }
  .decor {
    position: absolute;
    inset: 0;
    width: 1200px;
    height: 794px;
  }
  .initial {
    position: absolute;
    left: 272px;
    top: 140px;
    margin: 0;
    font-weight: 400;
    font-size: 160px;
    line-height: 1;
    color: var(--leaf-green);
  }
  .line {
    position: absolute;
    margin: 0;
    white-space: nowrap;
    line-height: 1;
  }
  .line--join {
    left: 330px;
    top: 230px;
    font-size: 56px;
    color: var(--pale-green);
  }
  .line--soiree {
    left: 316px;
    top: 284px;
    font-size: 56px;
    color: var(--glow-blue);
    text-shadow: 0 0 14px rgba(46, 166, 230, 0.8);
  }
  .line--soiree .on {
    font-size: 46px;
    color: var(--leaf-green);
    text-shadow: none;
    margin-left: 12px;
  }
  .line--date {
    left: 316px;
    top: 336px;
    font-size: 37px;
    color: var(--leaf-green);
  }
  .line--date .day {
    font-size: 62px;
    color: var(--glow-blue);
    text-shadow: 0 0 14px rgba(46, 166, 230, 0.8);
    margin-left: 10px;
  }
  .line--time {
    left: 328px;
    top: 404px;
    font-size: 36px;
    color: var(--leaf-green);
  }
  .line--venue {
    left: 266px;
    top: 464px;
    font-size: 25px;
    color: var(--ice-white);
  }
  .line--venue .at {
    font-size: 36px;
    color: var(--leaf-green);
    margin-right: 16px;
  }
  .brand-card {
    position: absolute;
    left: 672px;
    top: 664px;
    width: 528px;
    height: 130px;
    box-sizing: border-box;
    padding: 0 28px;
    background: var(--card-white);
    display: flex;
    flex-direction: column;
    justify-content: center;
    gap: 12px;
  }
  .brand {
    display: flex;
    align-items: center;
    gap: 14px;
    white-space: nowrap;
    line-height: 1;
  }
  .brand--crestwork .mark {
    width: 30px;
    height: 30px;
    border-radius: 50%;
    background: var(--crestwork-blue);
  }
  .brand--crestwork .name {
    font-size: 34px;
    color: var(--crestwork-blue);
    text-transform: uppercase;
    letter-spacing: 1px;
  }
  .brand--harbourline .mark {
    width: 20px;
    height: 20px;
    background: var(--harbourline-orange);
    margin: 0 5px;
  }
  .brand--harbourline .name {
    font-size: 22px;
    color: var(--harbourline-orange);
  }
</style>
</head>
<body>
<main class="invitation">
  <svg class="decor" viewBox="0 0 1200 794" aria-hidden="true">
    <defs>
      <radialGradient id="treeGlow" cx="50%" cy="55%" r="50%">
        <stop offset="0%" stop-color="var(--tree-green)" stop-opacity="0.75"/>
        <stop offset="55%" stop-color="var(--tree-blue)" stop-opacity="0.35"/>
        <stop offset="100%" stop-color="#000" stop-opacity="0"/>
      </radialGradient>
      <radialGradient id="goldSweep" cx="0%" cy="0%" r="100%">
        <stop offset="0%" stop-color="var(--gold)" stop-opacity="0.45"/>
        <stop offset="100%" stop-color="var(--gold)" stop-opacity="0"/>
      </radialGradient>
      <linearGradient id="leafBand" x1="0" y1="0" x2="1" y2="0">
        <stop offset="0%" stop-color="#3f8f2c"/>
        <stop offset="100%" stop-color="#17401a" stop-opacity="0.2"/>
      </linearGradient>
      <linearGradient id="blueFloor" x1="0" y1="0" x2="1" y2="0">
        <stop offset="0%" stop-color="var(--tree-blue)" stop-opacity="0"/>
        <stop offset="50%" stop-color="var(--tree-blue)" stop-opacity="0.55"/>
        <stop offset="100%" stop-color="var(--tree-blue)" stop-opacity="0"/>
      </linearGradient>
    </defs>
    <rect x="0" y="0" width="440" height="420" fill="url(#goldSweep)" role="img" aria-label="Golden ribbon streamers sweeping from the top left corner"/>
    <path d="M0 560 C 120 600, 260 700, 330 794 L 0 794 Z" fill="url(#leafBand)"/>
    <path d="M0 520 C 200 560, 420 680, 560 794" fill="none" stroke="var(--gold)" stroke-width="2" opacity="0.6"/>
    <rect x="0" y="690" width="900" height="60" fill="url(#blueFloor)" opacity="0.7"/>
    <ellipse cx="950" cy="370" rx="190" ry="300" fill="url(#treeGlow)" role="img" aria-label="Sparkling swirl Christmas tree in green, blue and gold with a star on top"/>
  </svg>

  <h1 class="initial">j</h1>
  <p class="line line--join">oin Christmas</p>
  <p class="line line--soiree">soiree<span class="on">on</span></p>
  <p class="line line--date">December<span class="day">6th</span></p>
  <p class="line line--time">from 4.30 - 7.30pm</p>
  <p class="line line--venue"><span class="at">At</span>218 Kowhai Valley Road, Ellerslie</p>

  <div class="brand-card">
    <div class="brand brand--crestwork">
      <span class="mark"></span>
      <span class="name">Crestwork Staffing</span>
    </div>
    <div class="brand brand--harbourline">
      <span class="mark"></span>
      <span class="name">The Harbourline Recruitment Company</span>
    </div>
  </div>
</main>
</body>
</html>
```